brightwell - Property Management DL Card

I am after a savvy designer to cut through junk mail! so many real estate agents use flyers to promote themselves and their business and usually sales. We are a property management firm (residential) and we want to represent landlords that have existing investment properties and need a quality agent to represent them. Can you help?
DL size, will be printed and delivered to mailboxes. For a look at our website go to www.brightwellhx.com.au. Keep it simple and clutter free.
it is to be double sided - with one side to be simple and clear - just our website, logo and telephone number on the back.
attached is our logo and our telephone number is 1300 82 41 96
the above are 2 essential elements to be included + our email address: admin@brightwellhx.com.au
also attached are our transparent price list

Target Market(s)
property investors,
people that manage properties themselves
Industry/Entity Type
Property Management
Other font styles liked:
- arial
Look and feel

```html
<!DOCTYPE html>
<html lang="en">
<head>
<meta charset="utf-8">
<title>brightwell – Property Management DL Card</title>
<link rel="stylesheet" href="https://fonts.googleapis.com/css2?family=Arimo:wght@400;700&display=swap">
<style>
  :root {
    --page: #ecebea;
    --card: #ffffff;
    --ink: #111111;
    --ink-soft: #222222;
    --muted: #c6c6c6;
    --brand: #3a3a3a;
    --grey-light: #b7b7b9;
    --grey-dark: #3b3b3e;
    --photo-a: #d9d6d1;
    --photo-b: #9c968f;
    --tick: #9a9a9a;
  }
  * { margin: 0; padding: 0; box-sizing: border-box; }
  html, body { width: 1200px; height: 900px; overflow: hidden; }
  body { background: var(--page); position: relative; font-family: "Arimo", Arial, sans-serif; color: var(--ink); }

  .card {
    position: absolute; width: 900px; height: 410px;
    background: var(--card); overflow: hidden;
    box-shadow: 0 2px 10px rgba(0,0,0,0.18);
  }
  .card--front { left: 30px; top: 25px; }
  .card--back { left: 270px; top: 465px; }
  .card__shapes { position: absolute; inset: 0; width: 100%; height: 100%; }

  .brand-name {
    position: absolute; width: 300px; text-align: center;
    font-size: 46px; font-weight: 400; color: var(--brand);
    line-height: 1; letter-spacing: 0.5px;
  }
  .card--front .brand-name { left: 93px; top: 50px; }
  .card--back .brand-name { left: 486px; top: 40px; }

  .headline { position: absolute; font-weight: 700; color: var(--ink); white-space: nowrap; line-height: 1.2; }
  .card--front .headline { left: 6px; top: 145px; font-size: 24px; }
  .card--back .headline { left: 452px; top: 165px; font-size: 22px; }

  .benefits { position: absolute; left: 184px; top: 200px; list-style: none; }
  .benefits li { display: flex; align-items: center; gap: 4px; font-size: 14px; font-weight: 700; color: var(--ink-soft); height: 24.5px; }
  .benefits svg { width: 16px; height: 18px; flex: none; }

  .call-label { position: absolute; left: 175px; top: 338px; font-size: 22px; font-weight: 700; color: var(--muted); line-height: 1.2; }
  .call-number { position: absolute; left: 130px; top: 366px; font-size: 32px; font-weight: 700; color: var(--ink); letter-spacing: 0.5px; line-height: 1.2; }

  .contacts { position: absolute; left: 502px; top: 284px; list-style: none; }
  .contacts li { display: flex; align-items: center; gap: 6px; font-size: 16px; color: var(--ink); height: 41px; }
  .contacts svg { width: 24px; height: 24px; flex: none; }
</style>
</head>
<body>

<section class="card card--front" aria-label="Card front">
  <svg class="card__shapes" viewBox="0 0 816 366" preserveAspectRatio="none">
    <defs>
      <linearGradient id="photo-front" x1="0" y1="0" x2="1" y2="1">
        <stop offset="0" stop-color="var(--photo-a)"/>
        <stop offset="1" stop-color="var(--photo-b)"/>
      </linearGradient>
    </defs>
    <polygon points="400,0 722,0 482,145" fill="var(--grey-light)"/>
    <polygon points="760,0 816,0 816,185" fill="var(--grey-dark)"/>
    <polygon role="img" aria-label="Photo of a bright modern living room with a round rug, armchair and fireplace" points="722,0 760,0 816,185 816,285 690,366 575,366 470,150" fill="url(#photo-front)"/>
    <polygon points="690,366 816,285 816,366" fill="var(--grey-light)"/>
  </svg>

  <p class="brand-name">brightwell</p>
  <h1 class="headline">We Specialise In Property Management</h1>
  <ul class="benefits">
    <li><svg viewBox="0 0 16 18"><path d="M2 10 L6 15 L14 2" fill="none" stroke="var(--tick)" stroke-width="3"/></svg>No postage and admin fees</li>
    <li><svg viewBox="0 0 16 18"><path d="M2 10 L6 15 L14 2" fill="none" stroke="var(--tick)" stroke-width="3"/></svg>No hidden extras</li>
    <li><svg viewBox="0 0 16 18"><path d="M2 10 L6 15 L14 2" fill="none" stroke="var(--tick)" stroke-width="3"/></svg>Excellent communication</li>
    <li><svg viewBox="0 0 16 18"><path d="M2 10 L6 15 L14 2" fill="none" stroke="var(--tick)" stroke-width="3"/></svg>Technology focussed</li>
  </ul>
  <p class="call-label">Call Us Today:</p>
  <p class="call-number">1300 82 41 96</p>
</section>

<section class="card card--back" aria-label="Card back">
  <svg class="card__shapes" viewBox="0 0 818 377" preserveAspectRatio="none">
    <defs>
      <linearGradient id="photo-back" x1="0" y1="0" x2="1" y2="1">
        <stop offset="0" stop-color="#efeeec"/>
        <stop offset="1" stop-color="#a9a39c"/>
      </linearGradient>
    </defs>
    <polygon points="0,0 212,0 0,122" fill="var(--grey-light)"/>
    <polygon role="img" aria-label="Photo of a white living room with a sofa, floor lamp and tall windows" points="0,122 212,0 285,0 385,255 330,377 150,377 0,175" fill="url(#photo-back)"/>
    <polygon points="0,175 150,377 0,377" fill="var(--grey-dark)"/>
    <polygon points="385,255 440,377 330,377" fill="var(--grey-light)"/>
  </svg>

  <p class="brand-name">brightwell</p>
  <h2 class="headline">Competitive Fees For All Budgets</h2>
  <ul class="contacts">
    <li><svg viewBox="0 0 24 24"><circle cx="12" cy="12" r="10.5" fill="none" stroke="var(--ink)" stroke-width="1.5"/><path d="M8 6.5 L10 6.5 L11 9.5 L9.5 10.5 Q11 13.5 13.5 14.5 L14.5 13 L17.5 14 L17.5 16 Q16 18 13 16.5 Q8.5 14 7 10 Q6.5 7.5 8 6.5 Z" fill="var(--ink)"/></svg>1300 82 41 96</li>
    <li><svg viewBox="0 0 24 24"><circle cx="12" cy="12" r="10.5" fill="none" stroke="var(--ink)" stroke-width="1.5"/><rect x="6" y="8" width="12" height="8.5" fill="none" stroke="var(--ink)" stroke-width="1.4"/><path d="M6 8 L12 13 L18 8" fill="none" stroke="var(--ink)" stroke-width="1.4"/></svg>admin@brightwellhx.com.au</li>
    <li><svg viewBox="0 0 24 24"><circle cx="12" cy="12" r="10.5" fill="none" stroke="var(--ink)" stroke-width="1.5"/><ellipse cx="12" cy="12" rx="4.5" ry="10.5" fill="none" stroke="var(--ink)" stroke-width="1.2"/><line x1="1.5" y1="12" x2="22.5" y2="12" stroke="var(--ink)" stroke-width="1.2"/></svg>www.brightwellhx.com.au</li>
  </ul>
</section>

</body>
</html>
```